Design some Business Cards for Mirela Voss Photography

Design Business Cards to match our website @ www.mirelavoss.example
Attachments include Logo and Example Cards with contact information.
Looking for an elegant look like our website.

```html
<!DOCTYPE html>
<html lang="en">
<head>
<meta charset="utf-8">
<title>Mirela Voss Photography – Business Card</title>
<link rel="stylesheet" href="https://fonts.googleapis.com/css2?family=Great+Vibes&family=Josefin+Sans:wght@400;600&display=swap">
<style>
  :root {
    --backdrop: #ece9e4;
    --card-black: #111111;
    --linen: #e2e1de;
    --circle: #f6f6f4;
    --plum: #4b3d49;
    --plum-frame: #6d5c6a;
    --strap: #1d221f;
    --strap-edge: #2c322e;
    --ink-light: #f4f1f3;
    --gold: #e0a13c;
    --camera-tone: #cfcfcb;
  }
  * { box-sizing: border-box; margin: 0; padding: 0; }
  html, body { width: 1200px; height: 871px; overflow: hidden; }
  body { background: var(--backdrop); position: relative; }

  .business-card {
    position: absolute; left: 370px; top: 36px;
    width: 460px; height: 800px;
    background: var(--card-black);
    box-shadow: 0 10px 30px rgba(0,0,0,.18);
  }
  .linen-panel {
    position: absolute; left: 30px; top: 30px; right: 30px; height: 330px;
    background: var(--linen);
  }
  .camera-medallion {
    position: absolute; left: 50%; top: 40px; transform: translateX(-50%);
    width: 250px; height: 250px; border-radius: 50%;
    background: var(--circle);
    display: flex; align-items: center; justify-content: center;
  }
  .camera-illustration {
    width: 130px; height: 190px; border-radius: 6px;
    background: linear-gradient(180deg, var(--camera-tone), #b8b8b3);
  }
  .plum-panel {
    position: absolute; left: 30px; top: 360px; right: 30px; bottom: 30px;
    background: var(--plum);
  }
  .strap {
    position: absolute; left: 50%; transform: translateX(-50%);
    top: 308px; bottom: 0; width: 118px;
  }
  .contact-box {
    position: absolute; left: 44px; right: 44px; top: 450px; height: 270px;
    background: var(--plum);
    border: 3px solid var(--plum-frame);
    text-align: center; color: var(--ink-light);
    padding-top: 14px;
  }
  .studio-name {
    font-family: "Great Vibes", cursive;
    font-size: 64px; line-height: 1; font-weight: 400;
  }
  .studio-name .studio-trade {
    display: block;
    font-family: "Josefin Sans", sans-serif;
    font-size: 15px; letter-spacing: 4px; font-weight: 600;
    margin-top: 2px;
  }
  .phone {
    font-family: "Josefin Sans", sans-serif;
    color: var(--gold); font-size: 30px; margin-top: 12px; letter-spacing: 1px;
  }
  .address {
    font-family: "Josefin Sans", sans-serif;
    font-size: 19px; line-height: 1.2; margin-top: 4px;
  }
  .divider {
    border: 0; border-top: 2px dotted var(--plum-frame);
    margin: 12px 28px 10px;
  }
  .website {
    font-family: "Josefin Sans", sans-serif;
    font-size: 21px; letter-spacing: .5px;
  }
</style>
</head>
<body>
  <article class="business-card">
    <div class="linen-panel">
      <div class="camera-medallion">
        <div class="camera-illustration" role="img" aria-label="Line illustration of a vintage twin-lens reflex camera"></div>
      </div>
    </div>
    <div class="plum-panel"></div>

    <svg class="strap" viewBox="0 0 118 462" preserveAspectRatio="none" aria-hidden="true">
      <path d="M0 40 Q0 0 40 0 H78 Q118 0 118 40 V462 H0 Z" fill="var(--strap)"/>
      <path d="M6 42 Q6 6 42 6 H76 Q112 6 112 42 V462" fill="none" stroke="var(--strap-edge)" stroke-width="2" stroke-dasharray="3 4"/>
      <circle cx="59" cy="32" r="11" fill="#0c0e0d"/>
      <circle cx="59" cy="32" r="5" fill="#2e3430"/>
    </svg>

    <section class="contact-box">
      <h1 class="studio-name">Mirela Voss<span class="studio-trade">PHOTOGRAPHY</span></h1>
      <p class="phone">555.014.2290</p>
      <p class="address">418 Alder Crest Ln.Maplewood<br>CA 95099</p>
      <hr class="divider">
      <p class="website">www.mirelavoss.example</p>
    </section>
  </article>
</body>
</html>
```